Lumen Vale Consulting business card

I have a new logo that was designed for me here on CraftHive. I am a medical device marketing consultant. The medical device industry is very professional, kind of dry, and can be a bit boring. But I'm in marketing so I want to look fresh and innovative, within the confines of the industry.

Please use the logo to its potential, making it colorful and visually interesting (I know, there's really only one color. I need some kind of interesting design element - maybe wraparound...

Target Market(s)

Marketing management in medical device companies.

Industry/Entity Type

Marketing

Requirements
Must have
• Melissa Corbin
Phone: 949-555-0143
Address: Harbor Crest, CA
melissa@lumenvaleconsulting.example
www.lumenvaleconsulting.example

```html
<!DOCTYPE html>
<html lang="en">
<head>
<meta charset="utf-8">
<title>Lumen Vale Consulting – Business Card</title>
<link rel="stylesheet" href="https://fonts.googleapis.com/css2?family=Montserrat:wght@500;600;700&display=swap">
<style>
  :root {
    --backdrop: #bcbdc0;
    --card: #000000;
    --panel: #0b0d0e;
    --panel-edge: #1b1d1f;
    --white: #ffffff;
    --accent: #74c4ea;
    --fan-light: rgba(160, 180, 192, 0.55);
    --fan-dark: rgba(70, 85, 95, 0.35);
  }
  * { box-sizing: border-box; margin: 0; padding: 0; }
  html, body {
    width: 1200px; height: 1196px; overflow: hidden;
    background: var(--backdrop);
    font-family: "Montserrat", Arial, sans-serif;
  }
  .canvas { position: relative; width: 1200px; height: 1196px; }

  .card {
    position: absolute; width: 640px; height: 371px;
    background: var(--card); border-radius: 58px; overflow: hidden;
  }
  .card--front { top: 195px; left: 283px; }
  .card--back { top: 628px; left: 291px; }

  /* Front */
  .brand-panel {
    position: absolute; left: 45px; top: 121px; width: 566px; height: 158px;
    background: var(--panel); border: 1px solid var(--panel-edge);
    display: flex; align-items: center; justify-content: center; gap: 16px;
  }
  .brand-square { width: 26px; height: 26px; background: var(--accent); }
  .brand-name {
    color: var(--white); font-weight: 600; font-size: 36px; letter-spacing: 0.2px;
  }

  /* Back */
  .holder {
    position: absolute; right: 371px; top: 76px;
    text-align: right; font-weight: 700; font-size: 36px; line-height: 40px;
    color: var(--white);
  }
  .holder__last { color: var(--accent); display: block; }
  .divider {
    position: absolute; left: 300px; top: 74px; width: 2px; height: 90px;
    background: var(--white);
  }
  .phone {
    position: absolute; left: 334px; top: 96px;
    display: flex; align-items: center; gap: 6px;
    color: var(--accent); font-weight: 700; font-size: 28px;
  }
  .phone svg { width: 36px; height: 40px; }

  .contact-list {
    position: absolute; left: 211px; top: 200px; list-style: none;
  }
  .contact-list li {
    display: flex; align-items: center; height: 32px;
    color: var(--white); font-weight: 500; font-size: 17px;
  }
  .contact-list svg { width: 22px; height: 22px; margin-right: 10px; flex: none; }
  .accent { color: var(--accent); }

  .fan {
    position: absolute; left: 0; bottom: 0; width: 190px; height: 185px;
    border-top-right-radius: 100%;
    background: radial-gradient(circle at 0 100%, var(--fan-light) 0%, var(--fan-dark) 75%, rgba(60,70,80,0.15) 100%);
  }
</style>
</head>
<body>
<main class="canvas">
  <section class="card card--front">
    <div class="brand-panel">
      <span class="brand-square"></span>
      <span class="brand-name">Lumen Vale Consulting</span>
    </div>
  </section>

  <section class="card card--back">
    <div class="fan" role="img" aria-label="Soft grey-blue petal fan decoration in the corner"></div>

    <h1 class="holder">Melissa <span class="holder__last">Corbin</span></h1>
    <span class="divider"></span>

    <div class="phone">
      <svg viewBox="0 0 24 28" aria-hidden="true">
        <path d="M6 2 C3 3 2 6 3 10 C5 17 9 23 14 26 C17 27 19 26 20 24 L17 19 C16 18 15 18 14 19 L12 20 C10 18 8 14 7 11 L9 10 C10 9 10 8 10 7 Z" fill="none" stroke="#ffffff" stroke-width="2" stroke-linejoin="round"/>
      </svg>
      <span>949-555-0143</span>
    </div>

    <ul class="contact-list">
      <li>
        <svg viewBox="0 0 24 24" aria-hidden="true"><path d="M12 2 C8 2 5 5 5 9 C5 14 12 22 12 22 C12 22 19 14 19 9 C19 5 16 2 12 2 Z" fill="var(--accent)"/><circle cx="12" cy="9" r="3" fill="#000"/></svg>
        Harbor Crest, CA
      </li>
      <li>
        <svg viewBox="0 0 24 24" aria-hidden="true"><rect x="2" y="5" width="20" height="14" fill="var(--accent)"/><path d="M2 5 L12 13 L22 5" fill="none" stroke="#000" stroke-width="1.6"/></svg>
        melissa@lumenvaleconsulting.example
      </li>
      <li>
        <svg viewBox="0 0 24 24" aria-hidden="true"><path d="M7 3 L7 19 L11 15 L14 21 L16 20 L13 14 L18 14 Z" fill="var(--accent)"/></svg>
        <span>www.lumen<span class="accent">vale</span>consulting.example</span>
      </li>
    </ul>
  </section>
</main>
</body>
</html>
```